Uni Camp Poster (Theme: Desert Oasis)

We require a poster design for our annual camp with the theme "desert oasis", please see the attached design brief for details.
We are the Coralline Fellowship (Cf), founded in 1996 at the Wexbridge Institute of Learning. As one of the largest social clubs at the Wexbridge Institute of Learning, Cf runs a variety of premier social and sporting events for University students.
Target Market(s)
18-19 year olds in Melbourne

```html
<!DOCTYPE html>
<html lang="en">
<head>
<meta charset="utf-8">
<title>Oasis: A Jorney Through the Sands — Coralline Fellowship Camp</title>
<link href="https://fonts.googleapis.com/css2?family=Almendra:wght@700&family=Roboto+Condensed:wght@400;700&display=swap" rel="stylesheet">
<style>
  :root {
    --stage: #d9d9d9;
    --sky-dark: #4a3b2a;
    --sky-warm: #9a6a3e;
    --glow: #e8b765;
    --palm: #3c4226;
    --sand: #c9a67a;
    --sand-light: #dcc09a;
    --ink-light: #ffffff;
    --chrome-hi: #f4f4f4;
    --chrome-mid: #9c9c9c;
    --chrome-lo: #4d4d4d;
    --band: rgba(70, 60, 50, 0.55);
  }
  * { margin: 0; padding: 0; box-sizing: border-box; }
  html, body {
    width: 1200px; height: 1200px; overflow: hidden;
    background: var(--stage);
  }
  .poster {
    position: absolute; left: 0; top: 262px;
    width: 1200px; height: 675px; overflow: hidden;
    font-family: "Roboto Condensed", Arial, sans-serif;
    color: var(--ink-light);
  }
  .scene-art {
    position: absolute; inset: 0;
    background:
      radial-gradient(ellipse 55% 30% at 52% 62%, rgba(232,183,101,0.85), transparent 70%),
      linear-gradient(180deg, var(--sky-dark) 0%, var(--sky-warm) 35%, var(--glow) 55%, var(--palm) 70%, var(--sand) 84%, var(--sand-light) 100%);
  }
  .presenter {
    position: absolute; left: 800px; top: 36px; width: 150px;
    text-align: center;
  }
  .presenter-name {
    font-size: 21px; line-height: 22px; font-weight: 400;
    text-transform: uppercase; letter-spacing: 0.5px;
  }
  .presenter-note {
    margin-top: 6px; font-size: 11px; font-weight: 400; text-transform: uppercase;
  }
  .affiliation-badge {
    position: absolute; left: 1060px; top: 34px;
    width: 70px; height: 70px; border-radius: 6px;
    background: rgba(255,255,255,0.85);
  }
  .title {
    position: absolute; left: 0; width: 1200px;
    text-align: center; white-space: nowrap;
    font-family: "Almendra", Georgia, serif; font-weight: 700;
    font-size: 132px; line-height: 1;
    background: linear-gradient(180deg, var(--chrome-hi) 0%, var(--chrome-mid) 45%, var(--chrome-lo) 60%, var(--chrome-hi) 100%);
    -webkit-background-clip: text; background-clip: text;
    color: transparent;
    filter: drop-shadow(3px 4px 2px rgba(0,0,0,0.8));
  }
  .title-line-one { top: 180px; padding-left: 40px; }
  .title-line-two { top: 305px; }
  .date-band {
    position: absolute; left: 170px; top: 462px; width: 790px; height: 44px;
    background: linear-gradient(90deg, transparent, var(--band) 12%, var(--band) 88%, transparent);
    border-bottom: 1px solid rgba(255,255,255,0.35);
    text-align: center;
    font-size: 28px; line-height: 44px; letter-spacing: 1.5px;
  }
  .date-band strong { font-weight: 700; }
  .date-band sup { font-size: 14px; vertical-align: 12px; }
  .date-band .small { font-size: 20px; }
  .price {
    position: absolute; left: 0; top: 522px; width: 1200px;
    padding-right: 110px;
    text-align: center; font-size: 21px; letter-spacing: 1.2px;
    text-transform: uppercase;
  }
  .price strong { font-weight: 700; }
</style>
</head>
<body>
  <main class="poster">
    <div class="scene-art" role="img" aria-label="Desert oasis at dusk with a glass geometric pyramid, palm trees around a pool, sand dunes, rocks, a standing figure and two cats under cloudy amber sky"></div>

    <div class="presenter">
      <p class="presenter-name">Coralline Fellowship</p>
      <p class="presenter-note">Presents</p>
    </div>
    <div class="affiliation-badge" aria-hidden="true"></div>

    <h1>
      <span class="title title-line-one">Oasis: A Jorney</span>
      <span class="title title-line-two">Through the Sands</span>
    </h1>

    <p class="date-band"><strong>11<sup>TH</sup></strong> <span class="small">TO</span> <strong>13<sup>TH</sup></strong> MARCH 2020</p>
    <p class="price"><strong>$155</strong> for <strong>members</strong> and <strong>$165</strong> for <strong>non-members</strong></p>
  </main>
</body>
</html>
```